BM PowerPoint Template Refresh

I'm looking to refresh our corporate presentation collateral, namely our base PowerPoint template. I need something that sparks, and gives the appearance of our contemporary firm that is hip, innovative, and modern. The project should provide for the various slide master templates with appropriately sized background images for slides in 4:3 and 16:9 formats

Target Market(s)

Investment banking prospect and clients which are typically in the high-tech industries of software, semiconductors,telecom, and telecom components

Industry/Entity Type

Investment Banking

Font styles to use
Other font styles liked:
• Goudy Old Style

Requirements
Must have
• - Must leverage current logo (red color is the standard, however portions of the logo or, color variations from our stock are possible for use), primary and secondary current colors. Non-section text is Goudy Old Style (headers and body text)
- The PPT template must have at least all of the LAYOUT options found in the Old BM Prez
- Options with and without the Brecon logo as a transparent background
- Need a final version in 16:9 and 4:3 formats
- Must be able to add footer information such as "Confidential Information", slide number, and date
Nice to have
• a few design ideas on the IP Engineering image found on slide 7 of the New BM Prez Attempt.ppt file

```html
<!DOCTYPE html>
<html lang="en">
<head>
<meta charset="utf-8">
<title>Brecon Advisors – Presentation Template</title>
<link href="https://fonts.googleapis.com/css2?family=Sorts+Mill+Goudy&display=swap" rel="stylesheet">
<style>
:root{
  --red:#d3202b;
  --red-deep:#a5141c;
  --blue:#2c5491;
  --blue-panel:rgba(44,80,140,.9);
  --ink:#333;
  --muted:#888;
  --stage:#2a3440;
  --white:#fff;
}
*{box-sizing:border-box;margin:0;padding:0}
html,body{width:1200px;height:3464px;overflow:hidden;background:var(--stage)}
body{font-family:"Sorts Mill Goudy",Georgia,serif;color:var(--ink);position:relative}
.slide{position:absolute;left:38px;width:1124px;height:632px;overflow:hidden;background:var(--white)}
.s1{top:16px}.s2{top:712px}.s3{top:1408px}.s4{top:2104px}.s5{top:2800px}

.brand{display:flex;align-items:center;gap:12px}
.brand-dot{border-radius:50%;background:var(--red);flex:none}
.brand-name{line-height:1;letter-spacing:.08em;color:var(--red)}

/* cover */
.s1 .photo{position:absolute;inset:0;background:linear-gradient(115deg,#c81f28 0%,#b41a22 45%,#8e1118 70%,#c62029 100%)}
.s1 .brand{position:absolute;left:50%;top:50%;transform:translate(-50%,-50%)}
.s1 .brand-dot{width:64px;height:64px;background:var(--white)}
.s1 .brand-name{color:var(--white);font-size:44px}

/* title */
.s2 .brand{position:absolute;left:50px;top:60px}
.s2 .brand-dot{width:34px;height:34px}
.s2 .brand-name{font-size:22px}
.s2 .disc{position:absolute;left:590px;top:-150px;width:640px;height:640px;border-radius:50%;background:var(--red)}
.s2 .photo{position:absolute;left:720px;top:0;width:404px;height:632px;background:linear-gradient(160deg,#f2f2f2,#9a9a9a 55%,#5a5a5a);clip-path:polygon(0 100%,0 45%,28% 12%,100% 0,100% 100%)}
.s2 h1{position:absolute;left:50px;top:250px;width:470px;font-weight:400;font-size:34px;line-height:1.25;color:var(--red);z-index:2}
.s2 .sub{position:absolute;left:50px;top:370px;font-size:24px;color:var(--blue)}
.s2 .speaker{position:absolute;left:50px;top:480px;font-size:15px;line-height:1.5}
.s2 .speaker span{display:block;color:var(--muted)}
.s2 .date{position:absolute;left:50px;top:565px;font-size:15px}

/* section */
.s3 .photo{position:absolute;inset:0;background:linear-gradient(90deg,#d9d9d9,#9d9d9d 45%,#6f6f6f 75%,#b8b8b8)}
.s3 .panel{position:absolute;left:170px;top:0;width:450px;height:560px;background:var(--blue-panel)}
.s3 h2{position:absolute;left:210px;top:210px;width:360px;font-weight:400;font-size:46px;line-height:1.18;color:var(--white)}
.s3 .sub{position:absolute;left:210px;top:380px;font-size:18px;color:#dbe3f0}
.s3 .ring{position:absolute;left:745px;top:190px}

/* content */
.s4 h2{position:absolute;left:50px;top:45px;font-weight:400;font-size:34px;color:var(--red)}
.s4 .corner{position:absolute;right:-70px;top:-70px;width:170px;height:170px;border-radius:50%;background:var(--red)}
.s4 .corner-dot{position:absolute;right:24px;top:22px;width:12px;height:12px;border-radius:50%;background:var(--white)}
.s4 ul{position:absolute;left:50px;top:150px;list-style:none;font-size:16px;line-height:1.65}
.s4 li::before{content:"•";margin-right:10px;color:var(--ink)}
.s4 li.l2::before,.s4 li.l4::before{content:"–"}
.l2{padding-left:30px}.l3{padding-left:70px}.l4{padding-left:110px}.l5{padding-left:150px}
.s4 .footer{position:absolute;left:50px;right:50px;bottom:18px;height:30px;border-top:1px solid #ddd;display:flex;justify-content:space-between;align-items:center;font-size:11px;color:var(--muted)}
.s4 .footer .brand-dot{width:16px;height:16px}
.s4 .footer .brand-name{font-size:11px}

/* closing */
.s5{background:linear-gradient(180deg,#fafafa,#dcdcdc)}
.s5 .head{position:absolute;left:50px;right:50px;top:150px;display:flex;align-items:center;gap:30px}
.s5 .head i{flex:1;height:1px;background:#cfcfcf}
.s5 .brand-dot{width:40px;height:40px}
.s5 .brand-name{font-size:28px}
.s5 .contacts{position:absolute;left:120px;right:120px;top:300px;display:flex;justify-content:space-between}
.contact{width:220px;text-align:center;font-size:16px;line-height:1.4}
.contact .ico{width:64px;height:64px;border-radius:50%;background:var(--red);margin:0 auto 22px;display:flex;align-items:center;justify-content:center}
</style>
</head>
<body>

<section class="slide s1">
  <div class="photo" role="img" aria-label="Red-tinted photo of a modern glass office tower"></div>
  <div class="brand"><span class="brand-dot"></span><span class="brand-name">BRECON ADVISORS</span></div>
</section>

<section class="slide s2">
  <div class="brand"><span class="brand-dot"></span><span class="brand-name">BRECON ADVISORS</span></div>
  <div class="disc"></div>
  <div class="photo" role="img" aria-label="Black and white photo of a glass office tower"></div>
  <h1>Presentation title here in this place can be into three lines</h1>
  <p class="sub">Subtitle here in blue</p>
  <p class="speaker">Speaker name<span>Designation</span></p>
  <p class="date">July 2022</p>
</section>

<section class="slide s3">
  <div class="photo" role="img" aria-label="Grey photo of coin stacks with a hand placing a coin and green seedlings"></div>
  <svg class="ring" width="90" height="90" viewBox="0 0 90 90"><circle cx="45" cy="45" r="32" fill="none" stroke="#d3202b" stroke-width="22"/></svg>
  <div class="panel"></div>
  <h2>Section divider slide title</h2>
  <p class="sub">Sub content</p>
</section>

<section class="slide s4">
  <h2>Slide title here</h2>
  <div class="corner"></div><div class="corner-dot"></div>
  <ul>
    <li>Bullet level 1</li>
    <li class="l2">Bullet level 2</li>
    <li class="l3">Bullet level 3</li>
    <li class="l4">Bullet level 4</li>
    <li class="l5">Bullet level 5</li>
  </ul>
  <div class="footer">
    <span>2 &nbsp;&nbsp; Date here</span>
    <span>Confidential information</span>
    <span class="brand"><span class="brand-dot"></span><span class="brand-name">BRECON</span></span>
  </div>
</section>

<section class="slide s5">
  <div class="head"><i></i><div class="brand"><span class="brand-dot"></span><span class="brand-name">BRECON ADVISORS</span></div><i></i></div>
  <div class="contacts">
    <div class="contact">
      <div class="ico"><svg width="28" height="28" viewBox="0 0 24 24"><path fill="#fff" d="M12 2a7 7 0 0 0-7 7c0 5 7 13 7 13s7-8 7-13a7 7 0 0 0-7-7zm0 9.5A2.5 2.5 0 1 1 12 6.5a2.5 2.5 0 0 1 0 5z"/></svg></div>
      2210 Harlow Avenue<br>Suite 400, Dallas, TX 75201
    </div>
    <div class="contact">
      <div class="ico"><svg width="28" height="28" viewBox="0 0 24 24"><path fill="#fff" d="M6.6 10.8a15 15 0 0 0 6.6 6.6l2.2-2.2a1 1 0 0 1 1-.25 11.4 11.4 0 0 0 3.6.57 1 1 0 0 1 1 1V20a1 1 0 0 1-1 1A17 17 0 0 1 3 4a1 1 0 0 1 1-1h3.5a1 1 0 0 1 1 1c0 1.250.2 2.450.57 3.570a1 1 0 0 1-.25 1z"/></svg></div>
      555.010.2400
    </div>
    <div class="contact">
      <div class="ico"><svg width="30" height="30" viewBox="0 0 24 24"><path fill="#fff" d="M6 3h9v5H6zM4 9h16a2 2 0 0 1 2 2v7H2v-7a2 2 0 0 1 2-2zm3 5v2h10v-2z"/></svg></div>
      555.010.6233
    </div>
    <div class="contact">
      <div class="ico"><svg width="30" height="30" viewBox="0 0 24 24"><path fill="#fff" d="M3 5h18v14H3zm2 2v.5l7 5 7-5V7l-7 5z"/></svg></div>
      info@BreconAdvisors.com
    </div>
  </div>
</section>

</body>
</html>
```